Promotional Poster for Music Achievement Program

I need a vertical 11x17 poster designed for a new program called Bright Path Music Achievement Program. The poster will be displayed in the lesson rooms and lobbies of music schools who use this program. The main headline of the flyer should be "Ask your teacher about Bright Path" And then the additional text should be "Love your lessons and practice like never before with 10 levels of achievement!" I would like to use the logo on the flyer, which I uploaded here. In terms of artwork/design, I am looking for a fun, but clean feel. The purpose of the program is for students to progress through ten levels of achievement as they climb higher and higher to mastery of their instrument at level 10, so a feel of climbing, leveling up, or advancing would be good. And of course, this is a music program, so any musical artwork involved would make sense. But again - nothing too busy or overwhelming!

Target Market(s)

Parents waiting in the lobby of a music school.

Industry/Entity Type

Promotional

Colors

Designer to choose colors to be used in the design.

Requirements
Must have
• - Bright Path logo
• - This headline: Ask your teacher about Bright Path
• - This additional text: Love your lessons and practice like never before with 10 levels of achievement!
Nice to have
• In terms of artwork/design, I am looking for a fun, but clean feel. The purpose of the program is for students to progress through ten levels of achievement as they climb higher and higher to mastery of their instrument at level 10, so a feel of climbing, leveling up, or advancing would be good. And of course, this is a music program, so any musical artwork involved would make sense. But again - nothing too busy or overwhelming!
Should not have
• Should not be too busy.

```html
<!DOCTYPE html>
<html lang="en">
<head>
<meta charset="utf-8">
<title>Bright Path Music Achievement Program Poster</title>
<link rel="stylesheet" href="https://fonts.googleapis.com/css2?family=Archivo+Black&family=Bebas+Neue&family=Montserrat:wght@300;600;700;800&display=swap">
<style>
  :root {
    --paper: #f7f7f7;
    --ink: #111111;
    --gold: #e4d39a;
    --gold-deep: #b89b4f;
    --lime: #cdd21c;
    --crimson: #c8102e;
    --maroon: #5a1420;
    --night: #1d1a24;
    --navy: #1f3b78;
    --crowd: #cfcfcf;
  }
  * { margin: 0; padding: 0; box-sizing: border-box; }
  html, body { width: 950px; height: 1200px; overflow: hidden; background: var(--paper); }
  .poster { position: relative; width: 950px; height: 1200px; overflow: hidden; background: var(--paper); }

  .brand {
    position: absolute; top: 52px; left: 0; width: 100%;
    display: flex; justify-content: center; align-items: center; gap: 16px;
    font-family: "Montserrat", sans-serif; font-weight: 700; font-size: 58px; color: var(--ink);
  }
  .brand-mark { width: 40px; height: 40px; background: var(--crimson); }

  .shapes { position: absolute; inset: 0; }

  .stage-art { position: absolute; left: 0; top: 180px; width: 950px; height: 800px; }

  .headline { position: absolute; left: 0; top: 0; width: 100%; text-align: center; }
  .ask-your {
    position: absolute; left: 210px; top: 370px; width: 520px;
    font-family: "Bebas Neue", sans-serif; font-size: 172px; line-height: 1;
    color: var(--gold); letter-spacing: -1px;
    background: linear-gradient(180deg, #fff6d6 0%, var(--gold) 45%, var(--gold-deep) 100%);
    -webkit-background-clip: text; background-clip: text; -webkit-text-fill-color: transparent;
    transform: rotate(-4deg) scaleY(1.08);
    filter: drop-shadow(0 4px 6px rgba(0,0,0,.6));
  }
  .teacher {
    position: absolute; left: 60px; top: 505px; width: 870px;
    font-family: "Archivo Black", sans-serif; font-size: 150px; line-height: 1;
    color: #ffffff; letter-spacing: 2px;
    transform: rotate(-5deg) scaleY(1.2);
    text-shadow: 0 0 14px rgba(255,255,255,.7), 0 6px 10px rgba(0,0,0,.55);
  }
  .about-tag {
    position: absolute; left: 195px; top: 680px;
    display: flex; align-items: center; gap: 12px;
    transform: rotate(-4deg);
  }
  .about-tag .stripes { width: 42px; height: 70px; background: repeating-linear-gradient(180deg, #fff 0 6px, transparent 6px 11px); }
  .about-tag .label {
    background: #fff; padding: 2px 18px 0;
    font-family: "Bebas Neue", sans-serif; font-size: 84px; line-height: 1; color: var(--ink);
  }

  .promise-band {
    position: absolute; left: -40px; top: 855px; width: 1030px; height: 92px;
    background: var(--ink); transform: rotate(-5deg);
    border-top: 3px solid #fff; outline: 3px solid var(--ink);
    display: flex; flex-direction: column; justify-content: center; align-items: center;
    font-family: "Montserrat", sans-serif; font-weight: 800; font-size: 25px; line-height: 1.2;
    color: var(--lime); text-transform: uppercase; text-align: center;
  }

  .crowd { position: absolute; left: 0; bottom: 0; width: 950px; height: 190px;
    background: linear-gradient(180deg, rgba(207,207,207,0) 0%, var(--crowd) 55%, #e2e2e2 100%); }

  .event { position: absolute; left: 0; top: 0; width: 100%; height: 100%; transform: rotate(-3deg); transform-origin: 470px 1040px; }
  .date-block { position: absolute; left: 150px; top: 985px; font-family: "Montserrat", sans-serif; color: var(--ink); }
  .date-block .day, .date-block .month { font-weight: 700; font-size: 25px; line-height: 1; }
  .date-block .date { font-weight: 800; font-size: 96px; line-height: .9; letter-spacing: -2px; }
  .year {
    position: absolute; left: 396px; top: 1100px;
    font-family: "Montserrat", sans-serif; font-weight: 300; font-size: 48px; color: var(--ink);
    transform: rotate(-90deg); transform-origin: left top;
  }
  .venue-pill {
    position: absolute; left: 470px; top: 990px; width: 385px; height: 64px;
    background: var(--lime); border-radius: 32px;
    display: flex; align-items: center; padding-left: 82px;
    font-family: "Montserrat", sans-serif; font-weight: 800; font-size: 26px; color: var(--ink);
  }
  .at-badge {
    position: absolute; left: 462px; top: 984px; width: 76px; height: 76px; border-radius: 50%;
    background: var(--ink); color: var(--lime);
    display: flex; align-items: center; justify-content: center;
    font-family: "Montserrat", sans-serif; font-weight: 800; font-size: 42px; padding-bottom: 6px;
  }
  .website {
    position: absolute; left: 0; top: 1162px; width: 100%; text-align: center;
    font-family: "Montserrat", sans-serif; font-weight: 600; font-size: 21px; letter-spacing: 7px; color: #333;
  }
</style>
</head>
<body>
<main class="poster">
  <div class="brand"><span class="brand-mark"></span><span>Bright Path</span></div>

  <svg class="stage-art" viewBox="0 0 950 800" role="img" aria-label="Paint splash with a concert stage, music notes and equaliser lights">
    <defs>
      <linearGradient id="splash" x1="0" y1="0" x2="1" y2="1">
        <stop offset="0" stop-color="#d41b4a"/>
        <stop offset=".35" stop-color="#5a1420"/>
        <stop offset=".6" stop-color="#1d1a24"/>
        <stop offset=".8" stop-color="#3a2a22"/>
        <stop offset="1" stop-color="#1f3b78"/>
      </linearGradient>
    </defs>
    <path fill="url(#splash)" d="M40 160 L180 60 L300 110 L420 20 L560 70 L700 40 L830 120 L930 190 L905 330 L940 470 L900 560 L930 700 L780 760 L620 790 L460 740 L300 790 L150 720 L20 760 L45 600 L10 470 L40 330 Z"/>
  </svg>

  <svg class="shapes" viewBox="0 0 950 1200" aria-hidden="true">
    <polygon points="805,105 865,115 810,150" fill="#5a1420"/>
    <polygon points="870,260 920,320 880,345" fill="#c8102e"/>
    <polygon points="750,315 790,315 760,345" fill="#2a0d12"/>
    <polygon points="0,345 40,330 10,395" fill="#c8102e"/>
    <polygon points="40,1035 95,1045 55,1075" fill="#f2c230"/>
    <polygon points="30,1100 60,1110 40,1125" fill="#f29a30"/>
  </svg>

  <h1 class="headline">
    <span class="ask-your">Ask Your</span>
    <span class="teacher">TEACHER</span>
    <span class="about-tag"><span class="stripes"></span><span class="label">About Bright Path</span><span class="stripes"></span></span>
  </h1>

  <p class="promise-band"><span>Love your lessons and practice like never before</span><span>with 10 levels of achievement!</span></p>

  <div class="crowd" role="img" aria-label="Silhouette of a cheering crowd with raised hands"></div>

  <section class="event">
    <div class="date-block">
      <p class="day">DAY GOES HERE</p>
      <p class="date">DATE</p>
      <p class="month">MONTH GOES HERE</p>
    </div>
    <p class="year">YEAR</p>
    <div class="venue-pill">Venue Goes Here</div>
    <div class="at-badge">at</div>
  </section>

  <p class="website">www.yourwebsite.com</p>
</main>
</body>
</html>
```